LBH Letterhead

I need letterhead for "lakeside birch holdings llc" ...

logo attached to project..

Company Info:
482 East Marlow Avenue, Suite 7B
Chicago, Illinois 60917
ofc 312-555-0148
facsimile 312-555-0193
www.lakesidebirchholdingsllc.example
info@lakesidebirchholdingsllc.example

I have multiple projects listed.. see below:

Business cards for lakeside birch holdings llc
letterhead "
envelopes "

Business cards for KV Commerce LLC
letterhead "
envelopes "

```html
<!DOCTYPE html>
<html lang="en">
<head>
<meta charset="utf-8">
<title>LBH Letterhead</title>
<link rel="stylesheet" href="https://fonts.googleapis.com/css2?family=Cinzel:wght@400&family=Gelasio:wght@400&display=swap">
<style>
  :root {
    --paper: #ffffff;
    --page-edge: #b9b9b9;
    --brand-blue: #1f4b8a;
    --ink: #2b2b2b;
  }
  html, body {
    margin: 0;
    padding: 0;
    width: 928px;
    height: 1200px;
    overflow: hidden;
    background: var(--paper);
  }
  .letterhead {
    position: relative;
    box-sizing: border-box;
    width: 928px;
    height: 1200px;
    background: var(--paper);
    border: 1px solid var(--page-edge);
  }
  .brand {
    position: absolute;
    left: 30px;
    top: 34px;
    display: flex;
    flex-direction: column;
    align-items: flex-start;
  }
  .brand-mark {
    width: 52px;
    height: 52px;
    margin-left: 92px;
    margin-bottom: 14px;
  }
  .brand-name {
    margin: 0;
    font-family: "Cinzel", serif;
    font-weight: 400;
    font-size: 16.5px;
    letter-spacing: 0.3px;
    color: var(--brand-blue);
    white-space: nowrap;
  }
  .contact {
    position: absolute;
    left: 620px;
    top: 31px;
    margin: 0;
    font-family: "Gelasio", serif;
    font-style: normal;
    font-size: 14.6px;
    line-height: 17px;
    color: var(--ink);
  }
  .contact span { display: block; white-space: nowrap; }
  .contact .web { color: var(--brand-blue); }
</style>
</head>
<body>
  <main class="letterhead">
    <header class="brand">
      <svg class="brand-mark" viewBox="0 0 52 52" aria-hidden="true">
        <circle cx="26" cy="26" r="24" fill="var(--brand-blue)"/>
      </svg>
      <p class="brand-name">Lakeside Birch Holdings llc</p>
    </header>
    <address class="contact">
      <span>482 East Marlow Avenue, Suite 7B</span>
      <span>Chicago, Illinois 60917</span>
      <span>Office: 312-555-0148</span>
      <span>Facsimile: 312-555-0193</span>
      <span class="web">www.lakesidebirchholdingsllc.example</span>
      <span>info@lakesidebirchholdingsllc.example</span>
    </address>
  </main>
</body>
</html>
```